I want a website to be designed for our new company, it's an import and export company for variety of things.

please see the attached Logo for our company and the Images for our different sections for our busienss

Target Market(s)

multiple

Coding

Coded - Design and coding required

Number of Pages Required

5+ page

Font styles to use
Sans Serif

Colors

Designer to choose colors to be used in the design.

Requirements
Must have
• KOR GLOBAL
• KOR global Trading & Contracting provides various services. The Company offers infrastructure construction, oil, enegy and gas services, agricultural projects, real estate development, travel and tourism, and food processing and trading.
• Civil contracting for infrastructure, residential and heavy projects. Through its main subsidiaries; distribution of general food products, construction chemicals including corrosion inhibitors and electrical machinery; provides catering and travel agency services; ownership and operation of a school; offers human sources services including manpower supply.
• Drilling and Gold Mines Used Machinery, All Kinds of Construction Machinery, Drilling Machines are manufactured and sold.
Nice to have
• good designa and beautiful colours, it has too look professional

```html
<!DOCTYPE html>
<html lang="en">
<head>
<meta charset="utf-8">
<title>KOR GLOBAL – Trading &amp; Contracting</title>
<link rel="stylesheet" href="https://fonts.googleapis.com/css2?family=Cinzel:wght@400;700&family=Lato:wght@300;400;700&family=Roboto:wght@500;700&display=swap">
<style>
:root{
  --black:#000;
  --ink:#0b0b0b;
  --card:#1f1f1f;
  --white:#fff;
  --muted:#9a9a9a;
  --red:#d8202a;
  --red-deep:#8e0f17;
  --indigo:#2e2a86;
  --line:#bbb;
}
*{box-sizing:border-box;margin:0;padding:0}
html,body{width:1200px;height:3658px;overflow:hidden;background:var(--black)}
body{position:relative;font-family:'Lato',sans-serif;color:var(--white)}
.abs{position:absolute}
.serif{font-family:'Cinzel',serif;font-weight:400;letter-spacing:1px}
.btn{position:absolute;display:flex;align-items:center;justify-content:center;font-family:'Roboto',sans-serif;font-weight:700;font-size:17px;color:var(--white);text-transform:uppercase}
.btn-red{background:var(--red)}
.btn-outline{border:2px solid var(--white)}

/* hero */
.hero{position:absolute;left:0;top:0;width:1200px;height:767px}
.hero-photo{position:absolute;inset:0;background:linear-gradient(180deg,#2a2a2a 0%,#5a5a5a 35%,#3e3e3e 60%,#1a1a1a 100%)}
.nav a{position:absolute;top:80px;font-family:'Roboto',sans-serif;font-weight:500;font-size:13px;color:var(--white);text-decoration:none;text-transform:uppercase}
.nav .active::after{content:"";position:absolute;left:0;right:0;bottom:-9px;height:2px;background:var(--red)}
.brand{position:absolute;left:490px;top:38px;width:220px;text-align:center}
.brand-dot{width:34px;height:34px;border:2px solid var(--white);border-radius:50%;margin:0 auto 10px}
.brand-name{font-family:'Lato',sans-serif;font-weight:400;font-size:17px;letter-spacing:4px;color:var(--white)}
.phone{position:absolute;left:902px;top:34px;font-family:'Roboto',sans-serif;font-weight:700;font-size:18px;display:flex;gap:6px;align-items:center}
.hero-welcome{position:absolute;top:302px;width:1200px;text-align:center;font-size:36px}
.hero-title{position:absolute;top:348px;width:1200px;text-align:center;font-size:54px;font-weight:700}
.arrow{position:absolute;top:362px;width:52px;height:52px;border-radius:50%;background:#d8d8d8;display:flex;align-items:center;justify-content:center}

/* about */
.section-title{position:absolute;width:1200px;text-align:center;font-size:33px}
.rule{position:absolute;left:568px;width:64px;height:2px;background:var(--line)}
.rule.red{background:var(--red)}
.about-copy{position:absolute;top:914px;left:100px;width:1000px;text-align:center;font-size:16px;line-height:31px;color:#e6e6e6;white-space:nowrap}

/* services */
.service{position:absolute;top:1230px;width:600px;height:453px;text-align:center}
.service h3{position:absolute;top:176px;width:100%;font-size:31px;font-weight:700}
.service p{position:absolute;top:226px;left:0;width:600px;font-size:14.5px;line-height:21px;white-space:nowrap}
.service .down{position:absolute;top:332px;left:279px;width:42px;height:42px;border:2px solid var(--white);border-radius:50%;display:flex;align-items:center;justify-content:center}

/* projects */
.project{position:absolute;top:1818px;width:301px;height:356px;background:var(--card)}
.project .shot{height:170px}
.project h4{margin:26px 28px 0;font-family:'Roboto',sans-serif;font-weight:700;font-size:18px;line-height:23px}
.project p{margin:12px 28px 0;font-size:11px;line-height:17px;color:#ddd;white-space:nowrap}
.project .more{display:block;margin:14px 28px 0;font-family:'Lato',sans-serif;font-weight:700;font-size:11px;color:var(--red)}

/* machines */
.machines{position:absolute;top:2218px;left:0;width:1200px;height:501px;overflow:hidden;background:#2a2a2a}
.machines h2{position:absolute;left:139px;top:80px;font-size:29px;line-height:36px}
.machines p{position:absolute;left:141px;top:194px;font-size:14px;line-height:27.5px;white-space:nowrap}

/* contact */
.contact{position:absolute;top:2719px;left:0;width:1200px;height:547px;background:linear-gradient(180deg,#141414 0%,#2b2b2b 55%,#0e0e0e 100%)}
.field{position:absolute;border:1px solid #5a5a5a;background:var(--black);font-size:14px;color:#ddd;padding:18px 20px}

/* footer */
.footer{position:absolute;top:3266px;left:0;width:1200px;height:392px;background:var(--ink)}
.fcol{position:absolute;top:58px}
.fcol h5{font-family:'Roboto',sans-serif;font-weight:500;font-size:18px;margin-bottom:18px}
.fcol li{list-style:none;font-size:15px;color:var(--muted);height:28.5px;display:flex;align-items:flex-start;gap:6px}
.fcol.info li{height:auto;margin-bottom:14px;gap:14px;line-height:18px}
.fcol.social li{height:36px;gap:18px}
.sicon{width:16px;height:16px;border-radius:50%;background:var(--white);margin-top:1px}
.copy{position:absolute;top:3610px;width:1200px;text-align:center;font-size:14px;color:#bdbdbd}
</style>
</head>
<body>

<header class="hero">
  <div class="hero-photo" role="img" aria-label="Offshore oil rig standing in the sea under a cloudy grey sky"></div>
  <svg class="abs" style="left:0;top:690px" width="1200" height="77" viewBox="0 0 1200 77">
    <path d="M0 10 L480 10 L600 67 L720 10 L1200 10 L1200 77 L0 77 Z" fill="#000"/>
    <path d="M0 6 L480 6 L600 63 L720 6 L1200 6" fill="none" stroke="#777" stroke-width="3"/>
  </svg>
  <nav class="nav">
    <a class="active" style="left:106px" href="#">Home</a>
    <a style="left:177px" href="#">About Us</a>
    <a style="left:274px" href="#">Services</a>
    <a style="left:369px" href="#">Projects</a>
    <a style="left:763px" href="#">News</a>
    <a style="left:832px" href="#">Testimonials</a>
    <a style="left:962px" href="#">Contact Us</a>
  </nav>
  <div class="brand"><div class="brand-dot"></div><div class="brand-name">KOR GLOBAL</div></div>
  <div class="phone">
    <svg width="16" height="16" viewBox="0 0 24 24"><path d="M6.6 10.8a15 15 0 0 0 6.6 6.6l2.2-2.2c.3-.3.7-.4 1-.2 1.1.4 2.3.6 3.6.6.6 0 1 .4 1 1V20c0 .6-.4 1-1 1A17 17 0 0 1 3 4c0-.6.4-1 1-1h3.5c.6 0 1 .4 1 1 0 1.3.2 2.5.6 3.6.1.3 0 .7-.2 1z" fill="#d8202a"/></svg>
    (685) 555 0192
  </div>
  <div class="hero-welcome serif">WELCOME TO</div>
  <div class="hero-title serif">KOR GLOBAL</div>
  <a class="btn btn-red" style="left:513px;top:430px;width:185px;height:53px">Learn More</a>
  <div class="arrow" style="left:105px"><svg width="18" height="18" viewBox="0 0 18 18"><path d="M12 2 L5 9 L12 16" fill="none" stroke="#222" stroke-width="2.4"/></svg></div>
  <div class="arrow" style="left:1038px"><svg width="18" height="18" viewBox="0 0 18 18"><path d="M6 2 L13 9 L6 16" fill="none" stroke="#222" stroke-width="2.4"/></svg></div>
</header>

<section>
  <h2 class="section-title serif" style="top:836px">WHO WE ARE</h2>
  <div class="rule" style="top:886px"></div>
  <p class="about-copy">Etiam eleifend metus vitae adipiscing semper mauris ipsum iaculis elit congue gravida elit mi egestas orci<br>Curabitur pede Maecenas aliquet velit vel turpis Mauris neque metus malesuada<br>Aec ultricies sit amet porttitor mattis enim In massa libero interdum nec interdum vel blandit sed nulla In<br>ullamcorper est eget tempor cursus neque mi consectetuer mi a ultricies massa est sed nisl Class aptent<br>taciti sociosqu ad litora torquent per conubia nostra per inceptos hymenaeos</p>
  <a class="btn btn-outline" style="left:515px;top:1103px;width:189px;height:54px">Learn More</a>
</section>

<section>
  <div class="service" style="left:0;background:linear-gradient(180deg,#3a3590,var(--indigo))" role="img" aria-label="Container port with cranes and stacked cargo, tinted indigo">
    <h3 class="serif">TRADING</h3>
    <p>Aa libero interdum nec interdum vel blandit sed nulla<br>In ullamcorper est eget tempor cursus neque mi<br>consectetuer mi a ultricies massa est sed nisl Class<br>aptent taciti sociosqu ad litora</p>
    <div class="down"><svg width="16" height="16" viewBox="0 0 16 16"><path d="M3 5 L8 10 L13 5" fill="none" stroke="#fff" stroke-width="2.2"/></svg></div>
  </div>
  <div class="service" style="left:600px;background:linear-gradient(180deg,#d4262e,#c81e27)" role="img" aria-label="Construction workers on a building site, tinted red">
    <h3 class="serif">CONTRACTING</h3>
    <p>Aa libero interdum nec interdum vel blandit sed nulla<br>In ullamcorper est eget tempor cursus neque mi<br>consectetuer mi a ultricies massa est sed nisl Class<br>aptent taciti sociosqu ad litora</p>
    <div class="down"><svg width="16" height="16" viewBox="0 0 16 16"><path d="M3 5 L8 10 L13 5" fill="none" stroke="#fff" stroke-width="2.2"/></svg></div>
  </div>
</section>

<section>
  <h2 class="section-title serif" style="top:1734px;font-size:31px">OUR PROJECTS</h2>
  <div class="rule" style="top:1778px"></div>
  <article class="project" style="left:126px">
    <div class="shot" style="background:linear-gradient(180deg,#6d8fa5,#c9d6dc 60%,#8a8a70)" role="img" aria-label="Yellow drilling rig working in a snowy forest"></div>
    <h4>Pellentesque faucibus Ut accumsan ultric</h4>
    <p>Duis quam Nam eget lacus Aliquam erat<br>volutpat Quisque dignissim congue leoMauris<br>vel lacus vitae felis vestibulum</p>
    <a class="more">READ MORE</a>
  </article>
  <article class="project" style="left:452px">
    <div class="shot" style="background:linear-gradient(180deg,#8c9699,#b9bdb8 50%,#6f7a6c)" role="img" aria-label="Aerial view of a large building complex"></div>
    <h4>Pellentesque faucibus Ut accumsan ultric</h4>
    <p>Duis quam Nam eget lacus Aliquam erat<br>volutpat Quisque dignissim congue leoMauris<br>vel lacus vitae felis vestibulum</p>
    <a class="more">READ MORE</a>
  </article>
  <article class="project" style="left:777px">
    <div class="shot" style="background:linear-gradient(180deg,#2d4a5a,#1f3d4c)" role="img" aria-label="Offshore drilling platform at sea seen from above"></div>
    <h4>Pellentesque faucibus Ut accumsan ultric</h4>
    <p>Duis quam Nam eget lacus Aliquam erat<br>volutpat Quisque dignissim congue leoMauris<br>vel lacus vitae felis vestibulum</p>
    <a class="more">READ MORE</a>
  </article>
</section>

<section class="machines">
  <div class="abs" style="left:480px;top:0;width:720px;height:501px;background:linear-gradient(160deg,#cfcfcf,#8a8a8a 45%,#4a4a4a)" role="img" aria-label="Black and white photo of tracked drilling machines on a quarry site"></div>
  <svg class="abs" style="left:0;top:0" width="710" height="501" viewBox="0 0 710 501">
    <defs><linearGradient id="machinesRed" x1="0" y1="0" x2="1" y2="1"><stop offset="0" stop-color="#2b2b2b"/><stop offset="0.45" stop-color="#7d1118"/><stop offset="1" stop-color="#b3151e"/></linearGradient></defs>
    <path d="M0 0 H703 L582 501 H0 Z" fill="url(#machinesRed)"/>
  </svg>
  <h2 class="serif">MANUFACTURING &amp; SOLD<br>DRILLING MACHINES</h2>
  <p>Nunc tempus felis vitae urna Vivamus porttitor neque<br>at volutpat rutrum purus nisi eleifend<br>Aibero a tempus libero lectus feugiat felis Morbi diam<br>mauris viverra in gravida eu mattis in ante Morbi eget<br>arcu Morbi porta libero id ullamcorper</p>
  <a class="btn btn-outline" style="left:146px;top:363px;width:165px;height:46px;font-size:14px">Learn More</a>
</section>

<section class="contact" role="img" aria-label="Dark photo of heavy machinery behind the contact form">
  <h2 class="section-title serif" style="top:74px;font-size:31px">CONTACT US</h2>
  <div class="rule red" style="top:118px"></div>
  <div class="field" style="left:177px;top:149px;width:408px;height:50px">Your Name</div>
  <div class="field" style="left:598px;top:149px;width:408px;height:50px">Phone</div>
  <div class="field" style="left:177px;top:211px;width:410px;height:50px">Email</div>
  <div class="field" style="left:598px;top:211px;width:410px;height:50px">City</div>
  <div class="field" style="left:177px;top:273px;width:827px;height:86px">Message</div>
  <a class="btn btn-red" style="left:510px;top:386px;width:196px;height:52px;font-size:20px;background:#c4161f">Submit</a>
</section>

<footer class="footer">
  <div class="fcol" style="left:183px">
    <h5>QUICK LINKS</h5>
    <ul><li>» Home</li><li>» About us</li><li>» Who We Serve</li><li>» Projects</li><li>» Services</li></ul>
  </div>
  <div class="fcol" style="left:383px">
    <h5>RESOURCES</h5>
    <ul><li>» News</li><li>» Testimonials</li><li>» Term of Use</li><li>» Sitemap</li><li>» Contact Us</li></ul>
  </div>
  <div class="fcol info" style="left:582px">
    <h5>CONTACT US</h5>
    <ul>
      <li><svg width="16" height="20" viewBox="0 0 16 20"><path d="M8 1a6 6 0 0 0-6 6c0 4.5 6 12 6 12s6-7.5 6-12a6 6 0 0 0-6-6z" fill="none" stroke="#bbb" stroke-width="1.6"/><circle cx="8" cy="7" r="2" fill="#bbb"/></svg><span>240 Harbor Lane Suite 12<br>Austin TX 78701</span></li>
      <li><svg width="16" height="16" viewBox="0 0 24 24"><path d="M6.6 10.8a15 15 0 0 0 6.6 6.6l2.2-2.2c.3-.3.7-.4 1-.2 1.1.4 2.3.6 3.6.6.6 0 1 .4 1 1V20c0 .6-.4 1-1 1A17 17 0 0 1 3 4c0-.6.4-1 1-1h3.5c.6 0 1 .4 1 1 0 1.3.2 2.5.6 3.6.1.3 0 .7-.2 1z" fill="none" stroke="#bbb" stroke-width="1.8"/></svg><span>+1 (917) 555-0148</span></li>
      <li><svg width="16" height="14" viewBox="0 0 16 14"><rect x="1" y="1" width="14" height="12" fill="none" stroke="#bbb" stroke-width="1.5"/><path d="M1 2 L8 8 L15 2" fill="none" stroke="#bbb" stroke-width="1.5"/></svg><span>info@korglobal.example</span></li>
    </ul>
  </div>
  <div class="fcol social" style="left:876px">
    <h5>SOCIAL MEDIA</h5>
    <ul>
      <li><span class="sicon"></span>Community</li>
      <li><span class="sicon"></span>Updates</li>
      <li><span class="sicon"></span>Network</li>
      <li><span class="sicon"></span>Gallery</li>
    </ul>
  </div>
</footer>
<div class="copy">© 2020 Company Name&nbsp; All right reserved</div>

</body>
</html>
```